Cool modern, tech Business card design

Looking for a new business card design for our Managed IT Services company. We would like 2 sides, with the logo one one side horizontally and then the information on the back in either vertical or horizontal. We want our colors from the logo incorporated but also would like to see the color gray in there as well.

Target Market(s)

IT, Information Technology, Tech, Service

Industry/Entity Type

It Service

Contact Information for Business Card

Carl Penner
Managing Partner
(P)555-271-4830 ext xxx
(F)555-271-4831
www.brixtelcore.com

Font styles to use
Sans Serif

Colors
959595
000000
ec1f27

Requirements
Must have
• Logo on one side with some nice design or pattern
• Information on back in either vertical or horizontal format
Nice to have
• For it to look cool, tech, modern, stand out.

```html
<!DOCTYPE html>
<html lang="en">
<head>
<meta charset="utf-8">
<title>Brixtel Core Business Card</title>
<link rel="stylesheet" href="https://fonts.googleapis.com/css2?family=Ubuntu:wght@400;500&display=swap">
<style>
  :root {
    --page-bg: #e6e6e6;
    --card-white: #ffffff;
    --ink-dark: #2b2b2b;
    --ink-gray: #959595;
    --brand-red: #ec1f27;
    --card-black: #1c1c1c;
    --pattern-mid: #2e2e2e;
    --pattern-light: #3a3a3a;
  }
  * { margin: 0; padding: 0; box-sizing: border-box; }
  html, body {
    width: 1125px;
    height: 1200px;
    overflow: hidden;
    background: var(--page-bg);
    font-family: "Ubuntu", sans-serif;
  }
  .card {
    position: absolute;
    left: 152px;
    width: 824px;
    height: 469px;
    border-radius: 24px;
    overflow: hidden;
  }
  .card-front { top: 99px; background: var(--card-white); }
  .card-back { top: 632px; background: var(--card-black); }

  .brand-lockup {
    position: absolute;
    left: 82px;
    top: 248px;
    display: flex;
    align-items: center;
    gap: 14px;
  }
  .brand-name {
    font-size: 50px;
    font-weight: 500;
    color: var(--ink-dark);
    letter-spacing: -0.5px;
  }
  .brand-square {
    width: 22px;
    height: 22px;
    border-radius: 5px;
    background: var(--brand-red);
  }

  .contact {
    position: absolute;
    left: 490px;
    top: 134px;
    color: var(--ink-dark);
  }
  .contact-name {
    font-size: 38px;
    font-weight: 500;
    letter-spacing: 0.5px;
    line-height: 1;
  }
  .contact-title {
    margin-top: 6px;
    font-size: 20px;
    color: var(--brand-red);
  }
  .contact-lines { margin-top: 16px; }
  .contact-line {
    display: flex;
    align-items: center;
    gap: 9px;
    font-size: 20px;
    line-height: 25px;
  }
  .contact-line svg { width: 18px; height: 18px; fill: var(--ink-dark); }
  .contact-web {
    margin-top: 14px;
    font-size: 18px;
    font-weight: 500;
    letter-spacing: 0.3px;
  }

  .accent-bar {
    position: absolute;
    left: 0;
    bottom: 0;
    width: 100%;
    height: 9px;
    display: flex;
  }
  .accent-red { width: 200px; background: var(--brand-red); margin-right: 3px; }
  .accent-dark { flex: 1; background: var(--card-black); }

  .back-pattern {
    position: absolute;
    inset: 0;
    background:
      linear-gradient(90deg, var(--card-black) 0%, var(--pattern-mid) 45%, var(--pattern-light) 70%, var(--pattern-mid) 100%);
    opacity: 0.9;
  }
  .back-lockup {
    position: absolute;
    right: 70px;
    bottom: 58px;
    display: flex;
    align-items: center;
    gap: 10px;
  }
  .back-lockup .brand-name {
    font-size: 26px;
    color: var(--card-white);
  }
  .back-lockup .brand-square { width: 14px; height: 14px; border-radius: 3px; }
</style>
</head>
<body>
  <section class="card card-front">
    <div class="brand-lockup">
      <span class="brand-name">brixtelcore</span>
      <span class="brand-square"></span>
    </div>

    <div class="contact">
      <div class="contact-name">CARL PENNER</div>
      <div class="contact-title">Managing Partner</div>
      <div class="contact-lines">
        <div class="contact-line">
          <svg viewBox="0 0 24 24" aria-hidden="true"><path d="M6.6 10.8c1.4 2.8 3.8 5.1 6.6 6.6l2.2-2.2c.3-.3.7-.4 1-.2 1.1.4 2.3.6 3.6.6.6 0 1 .4 1 1V20c0 .6-.4 1-1 1C10.6 21 3 13.4 3 4c0-.6.4-1 1-1h3.5c.6 0 1 .4 1 1 0 1.3.2 2.5.6 3.6.1.3 0 .7-.2 1l-2.3 2.2z"/></svg>
          <span>555-271-4830 ext 254</span>
        </div>
        <div class="contact-line">
          <svg viewBox="0 0 24 24" aria-hidden="true"><path d="M7 3h8l2 2v4H7V3zm-3 7h16a2 2 0 0 1 2 2v7H2v-7a2 2 0 0 1 2-2zm2 4v2h12v-2H6z"/></svg>
          <span>555-271-4831</span>
        </div>
      </div>
      <div class="contact-web">www.brixtelcore.com</div>
    </div>

    <div class="accent-bar">
      <div class="accent-red"></div>
      <div class="accent-dark"></div>
    </div>
  </section>

  <section class="card card-back">
    <div class="back-pattern" role="img" aria-label="Dark repeating wave pattern in shades of charcoal gray"></div>
    <div class="back-lockup">
      <span class="brand-name">brixtelcore</span>
      <span class="brand-square"></span>
    </div>
  </section>
</body>
</html>
```